Bramblewick Gardening Services. A6 flyer single sided

Need an A6 flyer designing. Single sided.
I am a gardener.
I do lawn mowing - one-off garden tidy ups or regular fortnightly visits.
All kinds of trees expertly felled, topped or pruned.
Hedge cutting.
Fencing replaced or repaired.
Fully insured.
Access to fully qualified and licenced tree arborist
07724 316048 or 01632 742918.

I have attached my business card and letter head logo.
I'm open to new designs without incorporating any of my artwork.

Industry/Entity Type

Gardener

```html
<!DOCTYPE html>
<html lang="en">
<head>
<meta charset="utf-8">
<title>Bramblewick Garden Service</title>
<link href="https://fonts.googleapis.com/css2?family=Rye&family=Archivo+Black&family=Arimo:wght@400;700&display=swap" rel="stylesheet">
<style>
  :root {
    --leaf-deep: #0b3a08;
    --leaf-dark: #145c0f;
    --leaf-mid: #2f8f1c;
    --leaf-bright: #63c72e;
    --leaf-glow: #a7ee5e;
    --title: #9be04f;
    --white: #ffffff;
  }
  html, body { margin: 0; padding: 0; overflow: hidden; }
  body { width: 900px; height: 1200px; background: var(--leaf-deep); }
  .flyer {
    position: relative;
    width: 900px; height: 1200px; overflow: hidden;
    background: radial-gradient(ellipse at 60% 45%, var(--leaf-mid) 0%, var(--leaf-dark) 45%, var(--leaf-deep) 100%);
    font-family: "Arimo", Arial, sans-serif;
    color: var(--white);
  }
  .brand-name {
    position: absolute; top: 22px; left: 0; width: 100%;
    margin: 0; text-align: center;
    font-family: "Rye", serif; font-weight: 400;
    font-size: 104px; letter-spacing: 2px; line-height: 1;
    color: var(--title);
  }
  .brand-tagline {
    position: absolute; top: 142px; left: 0; width: 100%;
    margin: 0; text-align: center;
    font-family: "Rye", serif; font-weight: 400;
    font-size: 50px; line-height: 1.1; color: var(--title);
  }
  .photo {
    position: absolute;
    box-shadow: 0 0 30px rgba(0,0,0,.45);
  }
  .photo-cottage {
    left: 40px; top: 785px; width: 290px; height: 205px;
    background: linear-gradient(160deg, #9fd97a 0%, #4f9c34 40%, #1f5e16 100%);
    opacity: .75;
  }
  .photo-topiary {
    left: 350px; top: 785px; width: 300px; height: 205px;
    background: linear-gradient(180deg, #5fae3a 0%, #2e7a1f 50%, #174d10 100%);
    opacity: .75;
  }
  .services {
    position: absolute; left: 42px; top: 214px; width: 820px;
    margin: 0; padding: 0; list-style: none;
    font-size: 37px; line-height: 1.18;
  }
  .services li {
    position: relative; padding-left: 36px; margin-bottom: 30px;
    text-shadow: 0 2px 6px rgba(0,0,0,.6);
  }
  .services li::before {
    content: ""; position: absolute; left: 4px; top: 16px;
    width: 11px; height: 11px; border-radius: 50%; background: var(--white);
  }
  .services .narrow { width: 760px; }
  .guarantee-badge {
    position: absolute; left: 684px; top: 792px; width: 190px; height: 190px;
  }
  .hedge-band {
    position: absolute; left: 0; bottom: 0; width: 900px; height: 200px;
    background: linear-gradient(180deg, rgba(20,80,12,0) 0%, #1d6a12 35%, #0e4009 100%);
  }
  .contact {
    position: absolute; left: 0; top: 1028px; width: 100%;
    text-align: center;
    font-family: "Archivo Black", sans-serif; font-size: 38px; line-height: 1.45;
    text-shadow: 0 3px 8px rgba(0,0,0,.7);
  }
  .contact p { margin: 0; }
</style>
</head>
<body>
  <main class="flyer">
    <div class="photo photo-cottage" role="img" aria-label="Photo of a cottage garden with neatly trimmed hedges and trees"></div>
    <div class="photo photo-topiary" role="img" aria-label="Photo of formal topiary garden with clipped hedges and paths"></div>

    <h1 class="brand-name">BRAMBLEWICK</h1>
    <h2 class="brand-tagline">Garden Service</h2>

    <ul class="services">
      <li>Hedge cutting</li>
      <li>Fencing replaced or repaired</li>
      <li class="narrow">All kinds of trees expertly felled,topped or pruned</li>
      <li class="narrow">Access to fully qualified and licensed tree arborist</li>
      <li class="narrow">One-off garden tidy ups or regular fortnightly visits</li>
      <li>Fully insured</li>
    </ul>

    <svg class="guarantee-badge" viewBox="0 0 190 190" aria-hidden="true">
      <defs>
        <radialGradient id="badgeFill" cx="40%" cy="35%" r="70%">
          <stop offset="0" stop-color="#8fe04a"/>
          <stop offset="1" stop-color="#2f8f1c"/>
        </radialGradient>
      </defs>
      <circle cx="95" cy="95" r="88" fill="url(#badgeFill)" stroke="#e9ffd8" stroke-width="6"/>
    </svg>

    <div class="hedge-band" role="img" aria-label="Row of leafy green hedge along the bottom edge"></div>

    <div class="contact">
      <p>Contact - Dan Harrow</p>
      <p>07724 316048 or 01632 742918</p>
    </div>
  </main>
</body>
</html>
```